Buch-/eBook-Cover für ein schickes Buch zum Thema Persönlichkeitsentwicklung/Business
Zielgruppe
Wir machen Bücher im Bereich Persönlichkeitsentwicklung & Spiritualität. Die Zielgruppe ist in der Regel weiblich, ab 35 Jahre, selbständig oder auf dem Weg in die Selbständigkeit. Sie mögen es elegant, denn sie lieben oder suchen die 'Fülle'.
Aufgabenstellung
Für dieses Buch ist es wichtig, dass Designelemente aus dem Lunar Pattern genutzt werden. Ich lade eine Datei mit gut laufenden Büchern von Borelio aus dem Bereich hoch, wo man das auch gut erkennen kann. Wenn Sie Stockfotos dafür benötigen, kaufen wir diese natürlich. Wichtig ist auch, dass das Buchcover elegant, edel und weiblich ist.
Der Titel des Buches:
Individueller Erfolg – Lunar Pattern im Business
Untertitel: Ihr leiser Pfad zu Klarheit und innerer Ruhe (kann auch mit aufs Cover)
Bitte verwenden Sie Designelemente aus dem Lunar Pattern auf dem Cover wegen dem Wiedererkennungseffekt. In dem Dokument, das ich beigefügt habe, finden Sie die derzeitigen Buchtitel zum Thema Lunar Pattern - alle haben Designelemente aus diesem Bereich auf dem Cover. Von den Covern in diesem Dokument können Sie sich gerne inspirieren lassen, die Titel laufen sehr gut.
Die Zielgruppe ist zumeist weiblich, wissbegierig, an Persönlichkeitsentwicklung, Spiritualität und auch Business bzw. Selbständigkeit interessiert. Die Zielgruppe ist über 40 Jahre alt und liest auch andere Bücher aus dem Bereich Spiritualität & Business, allerdings nicht so kitschige Engelchen, sondern sie sehen sich als moderner an.

```html
<!DOCTYPE html>
<html lang="de">
<head>
<meta charset="utf-8">
<title>Stiller Aufbruch – Lunar Pattern für Gründerinnen</title>
<link rel="stylesheet" href="https://fonts.googleapis.com/css2?family=Cinzel:wght@400;600&family=Cabin:wght@400&display=swap">
<style>
  :root {
    --sky-teal: #5e9fb8;
    --mid-blue: #4f82b3;
    --deep-indigo: #2d3a93;
    --night-indigo: #27307f;
    --thread-violet: rgba(190, 170, 230, 0.35);
    --chart-pale: rgba(215, 228, 245, 0.30);
    --frame: #1e2a55;
    --ink-light: #ffffff;
  }
  html, body {
    margin: 0;
    padding: 0;
    width: 850px;
    height: 1200px;
    overflow: hidden;
    background: #ffffff;
  }
  .cover {
    position: relative;
    width: 850px;
    height: 1200px;
    box-sizing: border-box;
    border: 2px solid var(--frame);
    overflow: hidden;
    color: var(--ink-light);
  }
  .cover-background {
    position: absolute;
    inset: 0;
    background: linear-gradient(180deg, var(--sky-teal) 0%, var(--mid-blue) 45%, var(--deep-indigo) 82%, var(--night-indigo) 100%);
  }
  .thread-art {
    position: absolute;
    left: 40px;
    top: 110px;
    width: 780px;
    height: 880px;
    border-radius: 48% 52% 44% 50% / 46% 50% 52% 48%;
    background: radial-gradient(ellipse at 50% 48%,
      rgba(255,255,255,0) 52%,
      var(--thread-violet) 62%,
      rgba(200,185,235,0.18) 72%,
      rgba(255,255,255,0) 78%);
  }
  .chart-art {
    position: absolute;
    left: 178px;
    top: 205px;
    width: 466px;
    height: 700px;
    background: radial-gradient(ellipse at 50% 50%, var(--chart-pale) 0%, rgba(215,228,245,0.16) 55%, rgba(215,228,245,0) 75%);
  }
  .title-block {
    position: absolute;
    left: 0;
    right: 0;
    top: 318px;
    margin: 0;
    text-align: center;
    font-family: "Cinzel", serif;
    font-weight: 400;
  }
  .title-line {
    display: block;
    line-height: 1;
    letter-spacing: 0.02em;
  }
  .title-small { font-size: 62px; }
  .title-large { font-size: 120px; margin-top: -8px; }
  .series-block {
    position: absolute;
    left: 0;
    right: 0;
    top: 512px;
    text-align: center;
    font-family: "Cinzel", serif;
    font-weight: 600;
    font-size: 46px;
    line-height: 66px;
    letter-spacing: 0.03em;
  }
  .series-block p { margin: 0; }
  .subtitle {
    position: absolute;
    left: 0;
    right: 0;
    top: 1038px;
    margin: 0;
    text-align: center;
    font-family: "Cabin", sans-serif;
    font-size: 28px;
    line-height: 40px;
  }
</style>
</head>
<body>
  <main class="cover">
    <div class="cover-background"></div>
    <div class="thread-art" role="img" aria-label="Fadengrafik: feine helle Linien zwischen Nägeln bilden den Umriss eines Kopfprofils"></div>
    <div class="chart-art" role="img" aria-label="Heller, halbtransparenter Lunar-Pattern-Chart aus Dreiecken und Quadraten, durch Linien verbunden"></div>

    <h1 class="title-block">
      <span class="title-line title-small">STILLER</span>
      <span class="title-line title-large">AUFBRUCH</span>
    </h1>

    <div class="series-block">
      <p>Lunar Pattern</p>
      <p>für Gründerinnen</p>
    </div>

    <p class="subtitle">Ihr leiser Pfad zu Klarheit<br>und innerer Ruhe</p>
  </main>
</body>
</html>
```